QVLT Meridian LLC Website

Basic website for a start up business in the defense and federal space. If we could have intelligence analysis and technology as a focus that would be great. Looking to use our core colors but a lighter set of web pages would be preferable

Target Market(s)

Defense

Coding

Coded - Design and coding required

Number of Pages Required

3 page

```html
<!DOCTYPE html>
<html lang="en">
<head>
<meta charset="utf-8">
<title>QVLT Meridian LLC</title>
<link href="https://fonts.googleapis.com/css2?family=Exo+2:wght@300;400&family=Montserrat:wght@400;500;600&family=Oswald:wght@400&display=swap" rel="stylesheet">
<style>
:root{
  --red:#c8062f;
  --pink:#f3d3da;
  --ink:#1b1b1f;
  --text:#2c2c33;
  --grey-band:#f4f6f8;
  --field:#eef1f4;
  --footer:#1c1820;
  --white:#ffffff;
}
*{margin:0;padding:0;box-sizing:border-box}
html,body{width:1200px;height:3890px;overflow:hidden}
body{position:relative;background:var(--white);font-family:"Montserrat",sans-serif;color:var(--text)}
.abs{position:absolute}
.wordmark{font-family:"Exo 2",sans-serif;font-weight:400;letter-spacing:3px;color:var(--white);white-space:nowrap}
.hero{left:0;top:0;width:1200px;height:546px;background:linear-gradient(180deg,#1a4a76 0%,#1f5584 45%,#31597a 75%,#46607a 100%);border-radius:0 0 60% 60%/0 0 14px 14px;overflow:hidden}
.hero-photo{position:absolute;inset:0;background:radial-gradient(ellipse 260px 330px at 600px 300px,rgba(200,205,215,.35),transparent 70%),linear-gradient(180deg,transparent 60%,rgba(190,195,205,.35) 100%)}
.nav{left:161px;top:27px;width:877px;height:41px}
.nav .wordmark{position:absolute;left:0;top:6px;font-size:24px}
.nav-links{position:absolute;right:0;top:0;display:flex;align-items:center;height:41px}
.nav-links span{font-size:12px;color:var(--white);margin-right:30px}
.nav-links .active{font-weight:600}
.btn-solid{background:var(--red);color:var(--white);font-size:12px;display:flex;align-items:center;justify-content:center}
.nav-links .btn-solid{width:128px;height:41px;margin:0}
.hero-title{left:0;top:262px;width:1200px;text-align:center;font-family:"Oswald",sans-serif;font-weight:400;font-size:45px;line-height:54px;color:var(--white)}
.hero-cta{left:536px;top:389px;width:128px;height:38px}
.btn{display:flex;align-items:center;justify-content:center;gap:14px;background:var(--pink);border-radius:3px;font-size:13px;font-weight:600;color:var(--ink);letter-spacing:.3px}
.btn i{display:block;width:30px;height:30px;background:var(--red);border-radius:4px;position:relative}
.btn i svg{position:absolute;left:9px;top:8px}
.deco-circle{left:-480px;top:810px;width:760px;height:760px;border-radius:50%;background:#fbf3f4}
h2{font-family:"Exo 2",sans-serif;font-weight:300;color:var(--ink);letter-spacing:.5px}
h2 .hl{color:var(--red)}
.center{left:0;width:1200px;text-align:center}
p{font-size:13.5px;line-height:24.7px}
.about-copy{left:190px;top:691px;width:820px;text-align:center}
.about-copy p+p{margin-top:12px}
.photo{border-radius:5px}
.sector-title{font-size:30px}
.sector-copy{font-size:12px;letter-spacing:.5px;line-height:24.7px;width:392px}
.card{left:576px;top:2064px;width:491px;height:399px;background:var(--white);box-shadow:0 8px 30px rgba(0,0,0,.14);padding:42px 32px}
.card h2{font-size:38px;line-height:47px}
.card p{margin-top:18px;font-size:13px;line-height:24.4px}
.cta-head{font-family:"Exo 2",sans-serif;font-weight:400;color:var(--red);font-size:30px;line-height:39px}
.band{left:0;top:2899px;width:1200px;height:686px;background:var(--grey-band)}
.panel-red{left:131px;top:2995px;width:305px;height:492px;background:var(--red);color:var(--white);padding:0 49px}
.panel-white{left:436px;top:2995px;width:631px;height:492px;background:var(--white)}
.panel-red h3,.panel-white h3{font-family:"Exo 2",sans-serif;font-weight:300;font-size:30px}
.panel-white h3{color:var(--ink);position:absolute;left:45px;top:36px}
.panel-red h3{position:absolute;left:49px;top:36px}
.info{position:absolute;left:49px;width:207px}
.info svg{position:absolute;left:0;top:2px}
.info b{display:block;margin-left:32px;font-size:12.5px;font-weight:600;letter-spacing:.3px}
.info span{display:block;margin-left:32px;font-size:12.5px;line-height:25px;margin-top:4px}
.rule{position:absolute;left:49px;width:207px;border-top:1px dashed rgba(255,255,255,.5)}
.social{position:absolute;top:411px;width:33px;height:33px;border:1.5px solid var(--white);border-radius:2px}
label{position:absolute;font-size:12px;color:var(--text)}
.field{position:absolute;background:var(--field)}
.footer{left:0;top:3585px;width:1200px;height:251px;background:var(--footer)}
.footer-links span{position:absolute;top:84px;font-size:13px;color:var(--white)}
.footer-links em{position:absolute;top:84px;font-style:normal;font-size:13px;color:#6a6570}
.footer .wordmark{position:absolute;left:0;width:1200px;text-align:center;top:160px;font-size:30px}
.copyright{left:0;top:3836px;width:1200px;height:54px;background:var(--red);color:var(--white);font-size:13px;display:flex;align-items:center;justify-content:center}
</style>
</head>
<body>

<section class="abs hero">
  <div class="hero-photo" role="img" aria-label="Capitol building dome photographed under a blue sky with a navy overlay"></div>
</section>
<nav class="abs nav">
  <div class="wordmark">QVLT MERIDIAN</div>
  <div class="nav-links">
    <span class="active">HOME</span><span>ABOUT US</span><span>SERVICES</span>
    <span class="btn-solid">CONTACT US</span>
  </div>
</nav>
<h1 class="abs hero-title">Creating Breakthrough Technologies And Capabilities<br>In Defence And Federal Space</h1>
<div class="abs btn-solid hero-cta">CONTACT US</div>

<div class="abs deco-circle"></div>

<h2 class="abs center" style="top:608px;font-size:36px">ABOUT <span class="hl">QVLT MERIDIAN</span></h2>
<div class="abs about-copy">
  <p>Lorem ipsum dolor sit amet, consectetur adipiscing elit. Ut ultrices feugiat urna. Cras porttitor non nulla vitae ultricies. Mauris malesuada metus in lobortis vulputate. Curabitur eleifend metus ac diam congue semper vitae non nunc. Mauris sed felis arcu. Donec eu iaculis felis. Duis pulvinar non neque vitae mattis. In egestas ut eros non aliquet.</p>
  <p>Suspendisse eu urna ac quam pretium venenatis. Vivamus tincidunt odio ut sapien dictum, vel vehicula nunc cursus. In nunc ligula, faucibus eget lacus nec, lobortis cursus sem. Mauris vitae scelerisque ipsum. Morbi euismod venenatis nibh nec elementum. Nunc auctor lectus in metus fermentum, a laoreet sem hendrerit. Morbi pulvinar ultrices nibh. Nulla ut dolor non nulla congue scelerisque. Quisque malesuada posuere leo ac bibendum.</p>
</div>
<div class="abs btn" style="left:522px;top:896px;width:156px;height:49px">READ MORE <i><svg width="12" height="14" viewBox="0 0 12 14"><path d="M3 1l6 6-6 6" fill="none" stroke="#fff" stroke-width="2"/></svg></i></div>

<h2 class="abs center" style="top:1043px;font-size:36px">SECTORS <span class="hl">WE SERVE</span></h2>
<p class="abs center" style="top:1096px;padding:0 290px">Lorem ipsum dolor sit amet, consectetuer adipiscing elit, sed diam nonummy nibh euismod dnt ut laoreet dolore magna aliquam erat volupat.</p>

<div class="abs photo" style="left:131px;top:1178px;width:470px;height:349px;background:linear-gradient(135deg,#4a5a4a 0%,#1f5577 40%,#2f8ab0 65%,#c98a4a 100%)" role="img" aria-label="Soldier touching a glowing holographic interface"></div>
<h2 class="abs sector-title" style="left:681px;top:1212px">DEFENCE</h2>
<p class="abs sector-copy" style="left:681px;top:1260px">Lorem ipsum dolor sit amet, consectetuer adipiscing elit, sed diam nonummy nibh euismod dnt ut laoreet dolore magna aliquam erat volupat. Ut wisi enim ad minim veniam, quis nostrud exerci tation ullamorper suscipit lobortis nisl ut aliquip ex ea coodo consuat. Duis autem vel eum iriure dolor in heerit in vulputate.</p>
<div class="abs btn" style="left:681px;top:1430px;width:155px;height:47px">READ MORE <i><svg width="12" height="14" viewBox="0 0 12 14"><path d="M3 1l6 6-6 6" fill="none" stroke="#fff" stroke-width="2"/></svg></i></div>

<h2 class="abs sector-title" style="left:133px;top:1612px">FEDERAL SPACE</h2>
<p class="abs sector-copy" style="left:133px;top:1658px">Lorem ipsum dolor sit amet, consectetuer adipiscing elit, sed diam nonummy nibh euismod dnt ut laoreet dolore magna aliquam erat volupat. Ut wisi enim ad minim veniam, quis nostrud exerci tation ullamorper suscipit lobortis nisl ut aliquip ex ea coodo consuat. Duis autem vel eum iriure dolor in heerit in vulputate.</p>
<div class="abs btn" style="left:133px;top:1829px;width:155px;height:48px">READ MORE <i><svg width="12" height="14" viewBox="0 0 12 14"><path d="M3 1l6 6-6 6" fill="none" stroke="#fff" stroke-width="2"/></svg></i></div>
<div class="abs photo" style="left:599px;top:1574px;width:468px;height:350px;background:linear-gradient(180deg,#0f5fa3 0%,#3d80b8 45%,#c9bda8 70%,#4b4a3c 100%)" role="img" aria-label="Capitol building in daylight against a blue sky"></div>

<div class="abs photo" style="left:131px;top:2024px;width:500px;height:479px;background:linear-gradient(135deg,#0a2a44 0%,#13506e 45%,#2aa3b8 65%,#0b2c45 100%)" role="img" aria-label="Hand touching a glowing data dashboard screen"></div>
<div class="abs card">
  <h2>INTELLIGENCE ANALYSIS<br><span class="hl">&amp; TECHNOLOGY</span></h2>
  <p>Lorem ipsum dolor sit amet, consectetuer adipiscing elit, sed diam nonummy nibh euismod dnt ut laoreet dolore magna aliquam erat volupat. Ut wisi enim ad minim veniam, quis nostrud exerci tation ullamorper suscipit lobortis nisl ut aliquip ex ea coodo consuat. Duis autem vel eum iriure dolor in heerit in vulputate ullamorper suscipit lobortis.</p>
</div>
<div class="abs btn" style="left:610px;top:2371px;width:164px;height:46px">CONTACT US <i><svg width="12" height="14" viewBox="0 0 12 14"><path d="M3 1l6 6-6 6" fill="none" stroke="#fff" stroke-width="2"/></svg></i></div>

<div class="abs center cta-head" style="top:2598px">Consectetuer Adipiscing Elit Sed Diam Nonummy Nibh<br>Euismod Tincidunt Ut Laoreet Dolore.</div>
<p class="abs center" style="top:2686px;padding:0 250px">Lorem ipsum dolor sit amet, consectetuer adipiscing elit, sed diam nonummy nibh euismod tincidunt ut laoreet dolore magna aliquam erat volutpat.Ut wisi enim ad minim.</p>
<div class="abs btn" style="left:518px;top:2754px;width:164px;height:47px">CONTACT US <i><svg width="12" height="14" viewBox="0 0 12 14"><path d="M3 1l6 6-6 6" fill="none" stroke="#fff" stroke-width="2"/></svg></i></div>

<div class="abs band"></div>
<aside class="abs panel-red">
  <h3>CONTACT US</h3>
  <div class="info" style="top:97px">
    <svg width="18" height="22" viewBox="0 0 18 22"><path d="M9 21s7-7.5 7-12.5A7 7 0 0 0 2 8.5C2 13.5 9 21 9 21z" fill="none" stroke="#fff" stroke-width="1.4"/><circle cx="9" cy="8.5" r="2.6" fill="none" stroke="#fff" stroke-width="1.4"/></svg>
    <b>ADDRESS</b><span>123, Building Name, Street City, State XY 123456</span>
  </div>
  <div class="rule" style="top:194px"></div>
  <div class="info" style="top:221px">
    <svg width="20" height="20" viewBox="0 0 20 20"><path d="M4 2l3 0 2 5-2 1.5a11 11 0 0 0 4.5 4.5L13 11l5 2v3a2 2 0 0 1-2 2A15 15 0 0 1 2 4a2 2 0 0 1 2-2z" fill="none" stroke="#fff" stroke-width="1.4"/></svg>
    <b>PHONE</b><span>+00 123 456 7890</span>
  </div>
  <div class="rule" style="top:289px"></div>
  <div class="info" style="top:316px">
    <svg width="22" height="16" viewBox="0 0 22 16"><rect x="1" y="1" width="20" height="14" fill="none" stroke="#fff" stroke-width="1.4"/><path d="M1 1l10 8 10-8" fill="none" stroke="#fff" stroke-width="1.4"/></svg>
    <b>EMAIL</b><span>info@qvltmeridian.com</span>
  </div>
  <div class="rule" style="top:384px"></div>
  <div class="social" style="left:52px"></div>
  <div class="social" style="left:98px"></div>
  <div class="social" style="left:145px"></div>
</aside>
<form class="abs panel-white">
  <h3>GET IN TOUCH</h3>
  <label style="left:47px;top:96px">First Name</label>
  <label style="left:328px;top:96px">Last Name</label>
  <div class="field" style="left:47px;top:118px;width:256px;height:41px"></div>
  <div class="field" style="left:328px;top:118px;width:256px;height:41px"></div>
  <label style="left:47px;top:182px">Phone</label>
  <label style="left:328px;top:182px">Email</label>
  <div class="field" style="left:47px;top:205px;width:256px;height:41px"></div>
  <div class="field" style="left:328px;top:205px;width:256px;height:41px"></div>
  <label style="left:47px;top:269px">Message</label>
  <div class="field" style="left:47px;top:293px;width:537px;height:80px"></div>
  <div class="btn" style="position:absolute;left:45px;top:405px;width:165px;height:47px">SUBMIT NOW <i><svg width="12" height="14" viewBox="0 0 12 14"><path d="M3 1l6 6-6 6" fill="none" stroke="#fff" stroke-width="2"/></svg></i></div>
</form>

<footer class="abs footer">
  <div class="footer-links">
    <span style="left:418px">HOME</span>
    <em style="left:504px">|</em>
    <span style="left:552px">ABOUT US</span>
    <em style="left:668px">|</em>
    <span style="left:714px">SERVICES</span>
  </div>
  <div class="wordmark">QVLT MERIDIAN</div>
</footer>
<div class="abs copyright">Copyright © 2022 QVLT MERIDIAN. All Rights Reserved.</div>

</body>
</html>
```